Zelmor Harbor Advisors Website

We are interested in developing a complete website and long term maintenance with the developer we choose through this contest.

Zelmor is a financial consulting company. We will have a website that capitalizes on the initial costs of retaining a client by providing additional services the client needs and tyically spend using 3rd parties.

The primary function of the website will be structured as a sales tool to retain and provide financial services to the client. Also, to provide other services that are integral to starting, building, and growing a business in order to increase creditibility and maintain client loyalty.

Through a combination of in-house "white label" services as well well chosen outside professional services as "affiliates".

The website home page must be a an instant curb-side appeal and representation of our desired extraordinary image. That image is a robust, innovative (zElmor), with a sophistication that creates an instant emotion of excitement and confidence that they have finally found that "needle in the haystack" they have been seeking. The feeling that they are compelled to take action lest they lose our contact information and are doomed to sink to the mediocrity that most business accept through a lack of effort and forsite.
Updates

Reason: Emails were going to the wrong account and I didn't receive any notices of questions or designs being posted.

Target Market(s)

Startup, growth and advancing companies seeking capital and other business services such as website and corporate image design, legal, marketing, asset management, investment and business consulting, etc.

Industry/Entity Type

Financial

Requirements
Must have
• We want to see your creativity
Nice to have
Should not have

```html
<!DOCTYPE html>
<html lang="en">
<head>
<meta charset="utf-8">
<title>Zelmor Harbor Advisors</title>
<link rel="stylesheet" href="https://fonts.googleapis.com/css2?family=PT+Sans:wght@400;700&family=Exo+2:ital,wght@1,300;1,400&family=Pinyon+Script&display=swap">
<style>
  :root {
    --black: #000000;
    --panel: #0b0b0b;
    --swoosh: #2a2a2a;
    --cyan: #00a9d6;
    --link: #29abe2;
    --text: #e6e6e6;
    --muted: #8c8c8c;
    --logo-grey: #58595b;
    --header-top: #f2f2f2;
    --header-bottom: #8f9093;
    --rule: #4a4a4a;
  }
  * { margin: 0; padding: 0; box-sizing: border-box; }
  html, body { width: 1200px; height: 905px; overflow: hidden; }
  body {
    position: relative;
    font-family: "PT Sans", sans-serif;
    background: linear-gradient(to bottom, var(--black) 0%, var(--black) 40%, #0d3a47 56%, var(--cyan) 76%, var(--cyan) 100%);
  }
  a { color: var(--link); text-decoration: none; }
  .abs { position: absolute; }

  .languages { left: 185px; top: 47px; font-size: 15px; display: flex; gap: 10px; }
  .search { left: 699px; top: 43px; display: flex; align-items: center; gap: 10px; }
  .search-label { color: var(--text); font-size: 17px; letter-spacing: 5px; }
  .search-field { width: 213px; height: 26px; border-radius: 5px; background: var(--link); border: none; }

  .masthead {
    left: 185px; top: 76px; width: 836px; height: 192px; border-radius: 3px;
    background: linear-gradient(to bottom, var(--header-top) 0%, #d2d3d5 45%, var(--header-bottom) 100%);
    overflow: hidden;
  }
  .brand-name {
    left: 24px; top: 20px; font-weight: 700; font-size: 118px; line-height: 1;
    color: var(--logo-grey); letter-spacing: -2px;
  }
  .brand-tagline {
    left: 116px; top: 142px; font-size: 17px; letter-spacing: 7.5px; color: #6d6e71;
  }
  .masthead-photo { left: 452px; top: 4px; }
  .account-links { right: 24px; top: 165px; font-size: 15px; }

  .frame { left: 149px; top: 280px; width: 903px; height: 600px; background: var(--black); border-radius: 0 0 30px 30px; }
  .stage {
    left: 175px; top: 294px; width: 857px; height: 527px;
    background: linear-gradient(to bottom, var(--panel) 0%, var(--panel) 78%, #1a6f88 90%, var(--cyan) 100%);
    border-radius: 0 0 8px 8px; overflow: hidden;
  }
  .stage-swoosh { left: 0; top: 0; }

  .side-nav-card { left: 194px; top: 304px; width: 218px; height: 481px; background: var(--black); border-radius: 8px; overflow: hidden; }
  .side-nav { left: 224px; top: 328px; width: 173px; list-style: none; }
  .side-nav li { position: relative; height: 42px; border-bottom: 2px solid var(--rule); padding: 5px 0 0 7px; font-size: 15.5px; }
  .side-nav li::after { content: ""; position: absolute; right: 15px; top: 15px; width: 8px; height: 8px; border-radius: 50%; background: var(--link); }
  .side-brand { left: 194px; top: 648px; width: 218px; text-align: center; }
  .side-brand-name { font-weight: 700; font-size: 44px; line-height: 1; color: #8a8b8d; }
  .side-brand-tagline { font-size: 7.5px; letter-spacing: 3px; color: #8a8b8d; margin-top: 3px; padding-left: 50px; }
  .mail-icon { left: 275px; top: 727px; }

  .welcome { left: 432px; top: 324px; width: 340px; }
  .welcome h1 { font-weight: 400; color: var(--link); font-size: 21px; line-height: 1.2; }
  .welcome h1 small { font-size: 14.5px; }
  .welcome p { color: var(--text); font-size: 12.3px; line-height: 16px; margin-top: 8px; }
  .welcome h1 + p { margin-top: 10px; }
  .signature { left: 612px; top: 560px; width: 156px; text-align: right; font-family: "Pinyon Script", cursive; font-size: 30px; color: var(--text); letter-spacing: 5px; }
  .team-photo { left: 432px; top: 613px; }

  .investor-card { left: 796px; top: 295px; width: 201px; height: 490px; border-radius: 8px; overflow: hidden; background: var(--black); }
  .investor-heading { left: 816px; top: 326px; font-family: "Exo 2", sans-serif; font-style: italic; font-weight: 300; color: #7a7a7a; line-height: 0.9; }
  .investor-heading .line-small { display: block; font-size: 38px; }
  .investor-heading .line-big { display: block; font-size: 68px; font-weight: 400; margin-left: 4px; }
  .investor-link { left: 796px; top: 480px; width: 201px; text-align: center; font-size: 19px; }
  .investor-photo { left: 814px; top: 522px; }

  .scrollbar { left: 1006px; top: 306px; width: 15px; height: 489px; border-radius: 8px; background: linear-gradient(to right, #1c1c1c, #4d4d4d, #1c1c1c); }
  .scrollbar-thumb { left: 3px; top: 24px; width: 8px; height: 32px; border-radius: 4px; background: #6f8791; }

  .footer { left: 182px; top: 843px; width: 845px; display: flex; font-size: 14.8px; color: var(--muted); }
  .footer-copy { width: 284px; }
  .footer-note { width: 290px; }
  .footer-links a { color: var(--link); }
  .footer-links span { color: var(--muted); margin: 0 4px; }
</style>
</head>
<body>

  <nav class="abs languages"><a href="#">English</a><a href="#">Hindi</a><a href="#">Spanish</a></nav>
  <form class="abs search"><span class="search-label">Seacrh:</span><input class="search-field" type="text" aria-label="Search"></form>

  <header class="abs masthead">
    <div class="abs brand-name">zElmor</div>
    <div class="abs brand-tagline">HARBOR ADVISORS</div>
    <svg class="abs masthead-photo" width="380" height="148" viewBox="0 0 380 148" role="img" aria-label="Photo of three smiling business colleagues">
      <defs>
        <linearGradient id="mastheadPhotoTone" x1="0" y1="0" x2="1" y2="0">
          <stop offset="0" stop-color="#5a4236"/>
          <stop offset="0.45" stop-color="#b89a88"/>
          <stop offset="1" stop-color="#d8c29a"/>
        </linearGradient>
      </defs>
      <path d="M60 0 H380 V140 C300 150 180 146 90 130 C20 118 -8 95 2 62 C12 30 34 8 60 0 Z" fill="url(#mastheadPhotoTone)"/>
    </svg>
    <div class="abs account-links"><a href="#">Login</a> <a href="#">Register</a></div>
  </header>

  <div class="abs frame"></div>
  <div class="abs stage">
    <svg class="abs stage-swoosh" width="857" height="527" viewBox="0 0 857 527" aria-hidden="true">
      <path d="M475 0 H857 V330 C790 220 720 100 475 0 Z" fill="var(--swoosh)"/>
    </svg>
  </div>

  <aside class="abs side-nav-card">
    <svg class="abs" style="left:0;top:0" width="218" height="260" viewBox="0 0 218 260" aria-hidden="true">
      <path d="M0 0 H196 C110 30 30 110 0 250 Z" fill="var(--swoosh)"/>
    </svg>
  </aside>
  <ul class="abs side-nav">
    <li><a href="#">Home</a></li>
    <li><a href="#">About Us</a></li>
    <li><a href="#">Services</a></li>
    <li><a href="#">Contact Us</a></li>
  </ul>
  <div class="abs side-brand">
    <div class="side-brand-name">zElmor</div>
    <div class="side-brand-tagline">HARBOR ADVISORS</div>
  </div>
  <svg class="abs mail-icon" width="53" height="37" viewBox="0 0 53 37" role="img" aria-label="Email">
    <rect x="1" y="1" width="51" height="35" rx="2" fill="#0a86b8" stroke="#0fa3d8" stroke-width="2"/>
    <path d="M4 4 L26.5 22 L49 4 M4 33 L20 17 M49 33 L33 17" stroke="var(--black)" stroke-width="3" fill="none"/>
  </svg>

  <section class="abs welcome">
    <h1>WELCOME <small>TO OUR COMPANY</small></h1>
    <p>Lorem ipsum dolor sit amet, consectetur adipisicing elit, sed do eiusmod tempor incididunt ut labore et dolore magna al Voluptate velit esse cillum dolore eu fugiat nulla pariatur. Excepteur sint... occaecat cupidatat non pro.</p>
    <p>Lorem ipsum dolor sit amet, consectetur adipisicing elit, sed do eiusmod tempor incididunt ut labore et dolore magna al Voluptate velit..</p>
    <p>Lorem ipsum dolor sit amet, consectetur adipisicing elit, sed do eiusmod tempor incididunt ut labore et dolore magna al Voluptate velit esse cillum dolore eu fugiat nulla pariatur. Excepteur sint... occaecat cupidatat non pro.</p>
  </section>
  <div class="abs signature">Jhon Doe</div>
  <svg class="abs team-photo" width="344" height="170" viewBox="0 0 344 170" role="img" aria-label="Black and white group photo of the advisory team in suits">
    <defs>
      <linearGradient id="teamPhotoTone" x1="0" y1="0" x2="0" y2="1">
        <stop offset="0" stop-color="#f4f4f4"/>
        <stop offset="0.35" stop-color="#8a8a8a"/>
        <stop offset="1" stop-color="#2a2a2a"/>
      </linearGradient>
    </defs>
    <rect width="344" height="170" fill="url(#teamPhotoTone)"/>
  </svg>

  <aside class="abs investor-card">
    <svg class="abs" style="left:0;top:0" width="201" height="320" viewBox="0 0 201 320" aria-hidden="true">
      <path d="M0 0 H201 V320 C160 200 110 90 0 0 Z" fill="var(--swoosh)"/>
      <path d="M0 0 H120 C70 20 30 40 0 50 Z" fill="#333"/>
    </svg>
  </aside>
  <div class="abs investor-heading"><span class="line-small">Looking</span><span class="line-big">FOR</span><span class="line-small">Investors</span></div>
  <a class="abs investor-link" href="#">Click here</a>
  <svg class="abs investor-photo" width="163" height="229" viewBox="0 0 163 229" role="img" aria-label="Photo of a hand holding a network cable in front of a market chart">
    <defs>
      <linearGradient id="investorPhotoTone" x1="0" y1="0" x2="1" y2="1">
        <stop offset="0" stop-color="#c9d3e6"/>
        <stop offset="0.5" stop-color="#7584a8"/>
        <stop offset="1" stop-color="#2b3658"/>
      </linearGradient>
    </defs>
    <rect width="163" height="229" rx="8" fill="url(#investorPhotoTone)"/>
  </svg>

  <div class="abs scrollbar"><div class="abs scrollbar-thumb"></div></div>

  <footer class="abs footer">
    <span class="footer-copy">©2011-2020 zElmor. All rights reserved.</span>
    <span class="footer-note">Lorem ipsum dolor sit amet, consectetur</span>
    <nav class="footer-links"><a href="#">Home</a><span>|</span><a href="#">About Us</a><span>|</span><a href="#">Services</a><span>|</span><a href="#">Contact Us</a></nav>
  </footer>

</body>
</html>
```